Stationery Design Project for Bramble Co

Hi All,

We need you to design stationary for a new online financial services business. We have already got the logo designed and it is attached. If you would like it in any other formats please let me know. If you could also if possible, match the fonts in your design to that on the logo’s provided.

What we need:
- Business Card
- A4 Letter head
- A4 Folders
- PPT template (Title page and regular page)

And what ever else you want to throw in.

We are in the process of getting the web site designed, however below is a list of websites which we like which will give you an understanding of the style that we are going for.

- plimo.com
- brambleroute.com
- tallowquay.com
- pelkwintry.com

I look forward to your seeing your design.

Industry/Entity Type

Financial

Requirements
Must have
• Outputs:
- Documents ready to print
- Generic editable information
- Pdf copies of the documents
- Word version of letterhead

```html
<!DOCTYPE html>
<html lang="en">
<head>
<meta charset="utf-8">
<title>Bramble Co – Folder</title>
<link href="https://fonts.googleapis.com/css2?family=Questrial&display=swap" rel="stylesheet">
<style>
  :root {
    --page-bg: #ecebe8;
    --paper: #ffffff;
    --brand-blue: #1680aa;
    --inside-blue: #0b7fab;
    --warm-light: #f7ac22;
    --warm-mid: #f39019;
    --warm-deep: #ee6b1e;
    --fold-line: #2a3a45;
    --text-light: #ffffff;
  }
  * { margin: 0; padding: 0; box-sizing: border-box; }
  html, body {
    width: 1200px; height: 900px; overflow: hidden;
    background: var(--page-bg);
    font-family: "Questrial", "Century Gothic", sans-serif;
  }
  .canvas { position: relative; width: 1200px; height: 900px; }

  .spread {
    position: absolute;
    box-shadow: 0 2px 6px rgba(0,0,0,.25);
    overflow: hidden;
  }
  .spread--inside { left: 483px; top: 326px; width: 667px; height: 471px; background: var(--inside-blue); }
  .spread--outside { left: 52px; top: 46px; width: 665px; height: 469px; background: var(--paper); }

  .fold { position: absolute; top: 0; bottom: 0; width: 1px; background: var(--fold-line); opacity: .7; }
  .spread--outside .fold { left: 332px; }
  .spread--inside .fold { left: 333px; }

  .art { position: absolute; left: 0; top: 0; }

  .band {
    position: absolute; left: 0; top: 197px; width: 100%; height: 77px;
    background: var(--brand-blue);
  }
  .band__brand {
    position: absolute; left: 62px; top: 21px; width: 70px;
    display: flex; flex-direction: column; align-items: center;
    color: var(--text-light);
  }
  .band__dot { width: 15px; height: 15px; border-radius: 50%; background: var(--warm-mid); }
  .band__name { font-size: 11px; margin-top: 5px; white-space: nowrap; }
  .band__contact {
    position: absolute; left: 135px; top: 25px;
    color: var(--text-light); font-size: 7.5px; line-height: 10px; font-style: normal;
  }
  .band__contact .phones { margin-top: 4px; }
  .band__web {
    position: absolute; right: 37px; top: 27px;
    display: flex; align-items: center; gap: 8px;
    color: var(--text-light); font-size: 19px;
  }
  .band__web .band__dot { width: 24px; height: 24px; }
</style>
</head>
<body>
<main class="canvas">

  <section class="spread spread--inside" aria-label="Folder inside with pocket">
    <div class="fold"></div>
    <svg class="art pocket" width="667" height="471" viewBox="483 326 667 471">
      <defs>
        <radialGradient id="pocketWarm" cx="1200" cy="860" r="380" gradientUnits="userSpaceOnUse">
          <stop offset="0" stop-color="var(--warm-deep)"/>
          <stop offset="1" stop-color="var(--warm-light)"/>
        </radialGradient>
        <filter id="pocketShadow" x="-10%" y="-10%" width="120%" height="120%">
          <feDropShadow dx="-2" dy="-3" stdDeviation="4" flood-color="#000" flood-opacity=".35"/>
        </filter>
      </defs>
      <path class="pocket__flap" role="img" aria-label="Warm orange decorative pocket artwork"
            d="M826 800 C846 720 890 650 960 615 C1020 588 1090 580 1152 580 L1152 800 Z"
            fill="url(#pocketWarm)" filter="url(#pocketShadow)"/>
      <line x1="816" y1="326" x2="816" y2="797" stroke="var(--fold-line)" stroke-opacity=".7"/>
    </svg>
  </section>

  <section class="spread spread--outside" aria-label="Folder outside">
    <svg class="art cover-art" width="665" height="469" viewBox="52 46 665 469">
      <defs>
        <radialGradient id="coverWarm" cx="58" cy="370" r="162" gradientUnits="userSpaceOnUse">
          <stop offset="0.5" stop-color="var(--warm-deep)"/>
          <stop offset="1" stop-color="var(--warm-light)"/>
        </radialGradient>
      </defs>
      <circle role="img" aria-label="Warm orange decorative cover artwork"
              cx="55" cy="357" r="160" fill="url(#coverWarm)"/>
    </svg>
    <div class="fold"></div>
    <div class="band">
      <div class="band__brand">
        <span class="band__dot"></span>
        <span class="band__name">Bramble Co</span>
      </div>
      <address class="band__contact">
        418 Harlow Street, 6th floor<br>
        Easton, PA 18042
        <div class="phones">T: 555-014-2280 &nbsp;|&nbsp; F: 555-014-2291</div>
      </address>
      <div class="band__web">
        <span class="band__dot"></span>
        <span class="band__url">brambleco.com</span>
      </div>
    </div>
  </section>

</main>
</body>
</html>
```